Masculine, visually appealing sales presentation for CPA firm

I have a basic power point that I use for sales presentations and I would like it to be updated to be more appealing and modern.

This is a presentation I give to real estate agents to help them close sales, save taxes, and resolve tax disputes. I would like the powerpoint to be updated to be more visually appealing. I have included the current powerpoint along with some of my logo files.

You don't have to use any of the pictures/clip art that is in the current power point. I only care that the words of the powerpoint make it to the new version.

Target Market(s)

Realtors, Real Estate Agents

Industry/Entity Type

Accounting

Requirements
Must have
• Visually appealing. I don't want it to look like I just took a template and made a normal powerpoint out of it. It should look custom.
Should not have
• Anything unprofessional, anything inconsistent with my brand

```html
<!DOCTYPE html>
<html lang="en">
<head>
<meta charset="utf-8">
<title>Taxation for Real Estate Professionals – Slide Board</title>
<link href="https://fonts.googleapis.com/css2?family=Signika:wght@400;600;700&family=Lato:ital,wght@0,400;0,700;1,700&display=swap" rel="stylesheet">
<style>
:root{
  --board:#e4e6f4;
  --slide:#f4f5f7;
  --navy:#1e4a86;
  --blue:#2d5d9c;
  --blue-soft:#5b83b8;
  --ink:#2b2f36;
  --muted:#a3a8b1;
  --rule:#4f78ad;
  --white:#ffffff;
}
*{margin:0;padding:0;box-sizing:border-box}
html,body{width:864px;height:1200px;overflow:hidden;background:var(--board)}
body{position:relative;font-family:"Lato",sans-serif;color:var(--ink)}
.slide{position:absolute;width:400px;height:224px;background:linear-gradient(180deg,#fafafb,var(--slide));overflow:hidden;box-shadow:0 4px 10px rgba(60,70,120,.18)}
.col-l{left:16px}.col-r{left:448px}
.row1{top:24px}.row2{top:257px}.row3{top:490px}.row4{top:722px}.row5{top:955px}
.abs{position:absolute}
.foot{position:absolute;left:0;right:26px;top:214px;border-top:1px solid var(--rule)}
.page{position:absolute;right:10px;top:210px;font:700 5.5px "Lato",sans-serif;color:var(--navy)}
.lorem{font-size:4.6px;line-height:1.45;color:var(--muted)}
.head{font-family:"Signika",sans-serif;font-weight:700;color:var(--navy)}
.tag{position:absolute;left:50%;transform:translateX(-50%);border:1px solid #c9d2e2;border-radius:3px;padding:1px 6px;background:#fff;font:700 9px "Signika",sans-serif;color:var(--navy);letter-spacing:.3px;white-space:nowrap}
.item{position:absolute;width:118px}
.item .num{font:700 10px "Signika",sans-serif;color:var(--navy);margin-right:3px}
.item .lbl{font-size:6.4px;color:var(--ink)}
.item .lorem{margin-left:20px;margin-top:1px;font-size:3.9px}
.photo{position:absolute}
.quote-mark{font:700 14px "Signika",sans-serif;color:var(--white);line-height:1}
.band-quote{position:absolute;color:#fff;font-size:6.8px;line-height:1.35;text-align:center;white-space:nowrap}
.plus{font:700 9px "Lato",sans-serif;color:var(--ink)}
.sec-title{font:700 10px "Signika",sans-serif;color:var(--navy);line-height:1.15;letter-spacing:.2px}
.money{position:absolute;font-family:"Signika",sans-serif;font-size:11px;color:#fff}
.money .v{position:absolute;left:126px;width:53px;border-bottom:1px solid #fff;padding-bottom:1px}
</style>
</head>
<body>

<!-- 1: Cover -->
<section class="slide col-l row1 cover">
  <div class="photo" role="img" aria-label="Bright modern office interior with city skyline windows" style="inset:0;background:linear-gradient(100deg,#cfd3d8 0%,#eceef0 45%,#f7f7f8 70%,#e3e6ea 100%)"></div>
  <div class="abs" style="left:0;right:0;top:104px;text-align:center;font:700 24px 'Signika',sans-serif;color:var(--navy)">The Oakline CPA</div>
  <div class="abs" style="left:0;right:0;top:140px;text-align:center;font-size:10px;color:var(--ink)">Helping you to achieve your goals</div>
  <div class="abs" style="left:0;right:0;top:212px;text-align:center;font-size:7px;color:#6f747b">National Guild of Tax Resolvers</div>
</section>

<!-- 2: Title -->
<section class="slide col-r row1 title">
  <h1 class="abs head" style="left:24px;top:54px;font-size:23px;line-height:1.2">Taxation for Real<br>Estate Professionals</h1>
  <div class="abs" style="left:24px;top:132px;font:400 12.5px 'Signika',sans-serif">Your Creative Subtitle</div>
  <p class="abs lorem" style="left:24px;top:150px;width:175px;color:#7d828a">Lorem ipsum dolor sit amet, consectetur adipisicing elit, sed do eiusmod tempor incididunt ut labore et dolore magna aliqua. Ut enim ad minim veniam, quis nostrud exercitation ullamco laboris nisi.</p>
  <div class="foot"></div><div class="page">01</div>
</section>

<!-- 3: Introductions -->
<section class="slide col-l row2 intro">
  <h2 class="abs head" style="left:0;right:0;top:19px;text-align:center;font-size:22px">Introductions</h2>
  <div class="abs" style="left:92px;width:62px;top:52px;border-top:1px solid #777"></div>
  <div class="abs" style="left:248px;width:62px;top:52px;border-top:1px solid #777"></div>
  <div class="abs" style="left:0;right:0;top:45px;text-align:center;font:400 12px 'Signika',sans-serif">Presented By</div>
  <div class="photo" role="img" aria-label="Portrait of the presenter" style="left:91px;top:83px;width:72px;height:66px;border-radius:50% 6px 6px 50%;background:linear-gradient(135deg,#5a5f52,#8b7b66 55%,#2f3340)"></div>
  <div class="abs" style="left:173px;top:87px;font-size:7.5px">Dale Harmon, CPA</div>
  <p class="abs" style="left:173px;top:100px;width:140px;font-size:4.8px;line-height:1.45;color:#555">I have been in the accounting business for over 12 years serving Vancouver, WA and Portland, OR. I specialize in helping entrepreneurs achieve their goals by turning the burden of accounting into a powerful tool to grow their business.</p>
  <div class="abs head" style="left:117px;top:171px;font-size:13px;line-height:1">&ldquo;</div>
  <div class="abs" style="left:117px;top:184px;font-size:6px;color:#555;white-space:nowrap">Don't be afraid to give up the good to go for the great.</div>
  <div class="abs" style="left:226px;top:197px;font-size:4.4px;color:#555">-J. D. Whitfield</div>
  <div class="abs head" style="left:270px;top:193px;font-size:13px;line-height:1">&rdquo;</div>
  <div class="foot"></div><div class="page">01</div>
</section>

<!-- 4: Table of contents -->
<section class="slide col-r row2 toc">
  <svg class="abs" style="left:180px;top:42px" width="40" height="64" viewBox="0 0 40 64" aria-hidden="true">
    <rect x="2" y="2" width="36" height="3" rx="1" fill="var(--ink)"/>
    <rect x="4" y="5" width="32" height="24" fill="#fff" stroke="var(--ink)" stroke-width="2"/>
    <rect x="8" y="9" width="24" height="16" fill="#f1e3c3"/>
    <circle cx="18" cy="17" r="4" fill="var(--ink)"/>
    <line x1="20" y1="31" x2="20" y2="64" stroke="#9aa0a8" stroke-width="1"/>
  </svg>
  <div class="abs" style="left:105px;top:107px;width:190px;height:24px;border:1px solid #aeb7c6;border-radius:5px;background:#fff;text-align:center;font:700 15px/22px 'Signika',sans-serif;color:var(--navy);letter-spacing:.5px">TABLE OF CONTENTS</div>
  <div class="foot"></div><div class="page">01</div>
</section>

<!-- 5: Taxation and client -->
<section class="slide col-l row3 list-3">
  <div class="tag" style="top:27px">TAXATION AND CLIENT</div>
  <div class="item" style="left:18px;top:72px"><span class="num">01.</span><span class="lbl">Sale of principal residence</span><p class="lorem">Lorem ipsum dolor sit amet, consectetur adipisicing elit, sed do eiusmod tempor inc</p></div>
  <div class="item" style="left:142px;top:72px"><span class="num">02.</span><span class="lbl">Federal tax lien on real estate</span><p class="lorem">Lorem ipsum dolor sit amet, consectetur adipisicing elit, sed do eiusmod tempor inc</p></div>
  <div class="item" style="left:277px;top:72px"><span class="num">03.</span><span class="lbl">Cancellation of debt</span><p class="lorem">Lorem ipsum dolor sit amet, consectetur adipisicing elit, sed do eiusmod tempor inc</p></div>
  <div class="photo" role="img" aria-label="Tax forms with a calculator reading tax time" style="left:0;right:0;top:131px;height:70px;background:linear-gradient(90deg,var(--navy) 0%,var(--blue) 35%,#7e98bd 55%,#d9dcdf 72%,#c8ccd0 100%)"></div>
  <div class="abs quote-mark" style="left:18px;top:140px">&ldquo;</div>
  <div class="band-quote" style="left:34px;top:150px;width:118px">Lorem ipsum dolor sit amet,<br>consectetur adipisic eiusmod<br>tempor incididunt uti.</div>
  <div class="abs quote-mark" style="left:140px;top:170px">&rdquo;</div>
  <div class="foot"></div><div class="page">01</div>
</section>

<!-- 6: Taxation and the realtor -->
<section class="slide col-r row3 list-9">
  <div class="tag" style="top:27px">TAXATION AND THE REALTOR</div>
  <div class="item" style="left:18px;top:62px"><span class="num">01.</span><span class="lbl">Estimated taxes</span><p class="lorem">Lorem ipsum dolor sit amet, consectetur adipisicing elit, sed do eiusmod tempor inc</p></div>
  <div class="item" style="left:142px;top:62px"><span class="num">02.</span><span class="lbl">Tax areas of special interest</span><p class="lorem">Lorem ipsum dolor sit amet, consectetur adipisicing elit, sed do eiusmod tempor inc</p></div>
  <div class="item" style="left:277px;top:62px"><span class="num">03.</span><span class="lbl">Home office</span><p class="lorem">Lorem ipsum dolor sit amet, consectetur adipisicing elit, sed do eiusmod tempor inc</p></div>
  <div class="item" style="left:18px;top:110px"><span class="num">04.</span><span class="lbl">Automobile</span><p class="lorem">Lorem ipsum dolor sit amet, consectetur adipisicing elit, sed do eiusmod tempor inc</p></div>
  <div class="item" style="left:142px;top:110px"><span class="num">05.</span><span class="lbl">Employ children</span><p class="lorem">Lorem ipsum dolor sit amet, consectetur adipisicing elit, sed do eiusmod tempor inc</p></div>
  <div class="item" style="left:277px;top:110px"><span class="num">06.</span><span class="lbl">Employ adult family</span><p class="lorem">Lorem ipsum dolor sit amet, consectetur adipisicing elit, sed do eiusmod tempor inc</p></div>
  <div class="item" style="left:18px;top:157px"><span class="num">07.</span><span class="lbl">Family employees</span><p class="lorem">Lorem ipsum dolor sit amet, consectetur adipisicing elit, sed do eiusmod tempor inc</p></div>
  <div class="item" style="left:142px;top:157px"><span class="num">08.</span><span class="lbl">Accounting Systems</span><p class="lorem">Lorem ipsum dolor sit amet, consectetur adipisicing elit, sed do eiusmod tempor inc</p></div>
  <div class="item" style="left:277px;top:157px"><span class="num">09.</span><span class="lbl">$$$$$$$$$$$$$$</span><p class="lorem">Lorem ipsum dolor sit amet, consectetur adipisicing elit, sed do eiusmod tempor inc</p></div>
  <div class="foot"></div><div class="page">01</div>
</section>

<!-- 7: Tax problem solutions -->
<section class="slide col-l row4 list-4">
  <div class="tag" style="top:26px">TAX PROBLEM SOLUTIONS</div>
  <div class="item" style="left:62px;top:56px;width:140px"><span class="num">01.</span><span class="lbl">Unfiled returns</span><p class="lorem">Lorem ipsum dolor sit amet, consectetur adipisicing elit, sed do eiusmod tempor inc</p></div>
  <div class="item" style="left:224px;top:56px;width:140px"><span class="num">02.</span><span class="lbl">Ostrich method</span><p class="lorem">Lorem ipsum dolor sit amet, consectetur adipisicing elit, sed do eiusmod tempor inc</p></div>
  <div class="item" style="left:62px;top:96px;width:140px"><span class="num">03.</span><span class="lbl">If you owe money</span><p class="lorem">Lorem ipsum dolor sit amet, consectetur adipisicing elit, sed do eiusmod tempor inc</p></div>
  <div class="item" style="left:224px;top:96px;width:140px"><span class="num">04.</span><span class="lbl">How about audits?</span><p class="lorem">Lorem ipsum dolor sit amet, consectetur adipisicing elit, sed do eiusmod tempor inc</p></div>
  <div class="photo" role="img" aria-label="Magnifying glass over a tax return document" style="left:0;right:0;top:131px;height:70px;background:linear-gradient(90deg,#cfd2d6 0%,#b9bec4 25%,#8ea3bf 45%,var(--blue) 60%,var(--navy) 100%)"></div>
  <div class="abs quote-mark" style="left:234px;top:142px">&ldquo;</div>
  <div class="band-quote" style="left:250px;top:152px;width:118px">Lorem ipsum dolor sit amet,<br>consectetur adipisic eiusmod<br>tempor incididunt uti.</div>
  <div class="abs quote-mark" style="left:356px;top:172px">&rdquo;</div>
  <div class="foot"></div><div class="page">01</div>
</section>

<!-- 8: Section one -->
<section class="slide col-r row4 section">
  <div class="photo" role="img" aria-label="Businessman in a tie holding blue blocks spelling taxation" style="inset:0;clip-path:polygon(256px 0,400px 0,400px 224px,144px 224px);background:linear-gradient(160deg,#f1f1f3 0%,#d9dbe0 40%,#2c3a6e 55%,#3f6fc2 70%,#e6e7ea 100%)"></div>
  <div class="abs plus" style="left:38px;top:28px">+</div>
  <div class="abs" style="left:36px;top:42px;font-size:4.6px;color:var(--muted)">Section One</div>
  <div class="abs sec-title" style="left:36px;top:49px">TAXATION AND CLIENT</div>
  <p class="abs lorem" style="left:36px;top:62px;width:118px">Lorem ipsum dolor sit amet, consectetur adipisicing elit, sed do eiusmod tempor incididunt ut labore et dolore magna aliqua. Ut enim ad minim veniam, quis nostrud exercitation ullamco laboris nisi ut aliquip ex ea</p>
  <div class="abs" style="left:36px;top:104px;font-size:7px;line-height:1.45">Closing controls commissions.<br>Liens control closings.</div>
  <div class="foot"></div><div class="page">01</div>
</section>

<!-- 9: Sale of principal residence -->
<section class="slide col-l row5 detail-left">
  <div class="abs plus" style="left:17px;top:68px">+</div>
  <div class="abs" style="left:17px;top:80px;font-size:4.6px;color:var(--muted)">01.</div>
  <div class="abs sec-title" style="left:17px;top:87px">SALE OF<br>PRINCIPAL RESIDENCE</div>
  <p class="abs lorem" style="left:17px;top:111px;width:112px">Lorem ipsum dolor sit amet, consectetur adipisicing elit, sed do eiusmod tempor incididunt ut labore et dolore magna aliqua. Ut enim ad minim veniam, quis nostrud exercitation ullamco laboris nisi ut aliquip ex ea</p>
  <div class="photo" role="img" aria-label="Handshake over house keys in blue tone" style="left:143px;top:0;right:0;bottom:0;background:linear-gradient(135deg,#3a67a4,var(--blue) 50%,#2a568f)"></div>
  <div class="abs" style="left:141px;top:66px;width:7px;height:21px;border-radius:0 4px 4px 0;background:#fff"></div>
  <div class="abs" style="left:141px;top:107px;width:7px;height:21px;border-radius:0 4px 4px 0;background:#fff"></div>
  <div class="abs" style="left:141px;top:148px;width:7px;height:21px;border-radius:0 4px 4px 0;background:#fff"></div>
  <svg class="abs" style="left:178px;top:70px" width="16" height="16" viewBox="0 0 16 16" aria-hidden="true"><path d="M2 8 L8 2 L14 8 M4 7 V14 H12 V7" fill="none" stroke="#fff" stroke-width="1.1"/></svg>
  <div class="abs" style="left:204px;top:74px;font-size:7.8px;color:#fff">Only one principal residence permitted.</div>
  <svg class="abs" style="left:178px;top:107px" width="16" height="16" viewBox="0 0 16 16" aria-hidden="true"><circle cx="5" cy="5" r="3" fill="none" stroke="#fff" stroke-width="1"/><circle cx="11" cy="5" r="3" fill="none" stroke="#fff" stroke-width="1"/><circle cx="8" cy="11" r="3" fill="none" stroke="#fff" stroke-width="1"/></svg>
  <div class="abs" style="left:204px;top:108px;font-size:7.8px;line-height:1.4;color:#fff">Exclusion of $250K of gain, or $500K<br>for married persons filing jointly.</div>
  <svg class="abs" style="left:178px;top:148px" width="16" height="16" viewBox="0 0 16 16" aria-hidden="true"><rect x="2" y="4" width="12" height="9" rx="1" fill="none" stroke="#fff" stroke-width="1"/><path d="M4 4 L11 1.5 L12 4 M10 8 H14" fill="none" stroke="#fff" stroke-width="1"/></svg>
  <div class="abs" style="left:204px;top:150px;font-size:7.8px;line-height:1.4;color:#fff">Must have been taxpayer's principal<br>residence for 2 of the last 5 years.</div>
  <div class="page" style="color:#fff">01</div>
  <div class="abs" style="left:143px;right:26px;top:214px;border-top:1px solid #fff"></div>
</section>

<!-- 10: Federal tax lien -->
<section class="slide col-r row5 detail-right">
  <div class="photo" role="img" aria-label="Small house model on stacks of banknotes in blue tone" style="left:0;top:0;width:257px;bottom:0;background:linear-gradient(180deg,#5a82b7 0%,var(--blue) 55%,#3a65a0 100%)"></div>
  <div class="money" style="left:30px;top:45px;width:180px">Selling price<span class="v" style="border:none">$200,000</span></div>
  <div class="money" style="left:30px;top:63px;width:180px">Less: Balance of PMM<span class="v">$100,000</span></div>
  <div class="money" style="left:30px;top:82px;width:180px">Excess cash<span class="v">$100,000</span></div>
  <div class="money" style="left:30px;top:100px;width:180px">Current tax on sale<span class="v">$20,000</span></div>
  <div class="abs" style="left:28px;top:120px;width:181px;height:15px;border:1px solid #fff;border-radius:4px;background:#fff"></div>
  <div class="money" style="left:31px;top:121px;width:180px;color:var(--ink)">Cash to IRS<span class="v" style="left:124px;border:none">$80,000</span></div>
  <svg class="abs" style="left:196px;top:136px" width="16" height="22" viewBox="0 0 16 22" aria-hidden="true"><path d="M4 1 C14 6 14 16 4 19 M4 19 L8 16 M4 19 L8 21" fill="none" stroke="#fff" stroke-width="1"/></svg>
  <div class="abs" style="left:166px;top:159px;width:80px;font:italic 700 6.2px/1.4 'Lato',sans-serif;color:#fff">Apply to old tax liabil ty, any excess would remain with taxpayer</div>
  <div class="abs plus" style="left:275px;top:68px">+</div>
  <div class="abs" style="left:275px;top:80px;font-size:4.6px;color:var(--muted)">02.</div>
  <div class="abs sec-title" style="left:275px;top:87px">FEDERAL TAX LIEN<br>ON REAL ESTATE</div>
  <p class="abs lorem" style="left:275px;top:111px;width:112px">Lorem ipsum dolor sit amet, consectetur adipisicing elit, sed do eiusmod tempor incididunt ut labore et dolore magna aliqua. Ut enim ad minim veniam, quis nostrud exercitation ullamco laboris nisi ut aliquip ex ea</p>
  <div class="abs" style="left:257px;right:26px;top:214px;border-top:1px solid var(--rule)"></div>
  <div class="page">01</div>
</section>

</body>
</html>
```